Calibrated NET Systems
Business card and Stationary
Project: Calibrated NET Systems
Calibrated NET Systems - Information Technology
Creative Brief
Professional
Dean Harlowe
Technical Consultant
Please leave the address part blank.
dean.harlowe@calnet.ca
www.calnet.ca

```html
<!DOCTYPE html>
<html lang="en">
<head>
<meta charset="utf-8">
<title>Calibrated NET Systems – Stationery</title>
<link href="https://fonts.googleapis.com/css2?family=Roboto:wght@400;500&display=swap" rel="stylesheet">
<style>
:root{
  --backdrop:#5a2f12;
  --paper:#ffffff;
  --ink:#222222;
  --muted:#8a8f96;
  --brand:#2a8fc4;
  --brand-light:#bfe3f5;
  --night:#0d0f12;
  --rule:#c9ced3;
  --mist:#e8ecef;
}
*{box-sizing:border-box;margin:0;padding:0}
html,body{width:1200px;height:622px;overflow:hidden}
body{background:var(--backdrop);font-family:"Roboto",Arial,sans-serif;color:var(--ink);position:relative}
.sheet,.envelope,.card{position:absolute;background:var(--paper);box-shadow:0 2px 6px rgba(0,0,0,.35);overflow:hidden}
.brand{display:flex;align-items:center;gap:5px;font-weight:500;color:var(--brand);white-space:nowrap;z-index:2}
.brand-mark{width:10px;height:10px;background:var(--brand);flex:none}
.brand--light{color:var(--paper)}
.brand--light .brand-mark{background:var(--brand-light)}
.foot{position:absolute;left:0;right:0;bottom:12px;display:flex;gap:18px;padding:0 16px;font-size:5.5px;line-height:1.5;color:var(--muted);z-index:2}

/* letterhead */
.letterhead{left:31px;top:72px;width:320px;height:440px}
.letterhead .band{position:absolute;left:0;top:0;width:100%;height:62px}
.letterhead .brand{position:absolute;left:16px;top:18px;font-size:11px}

/* fax */
.fax{left:384px;top:72px;width:336px;height:440px}
.fax .stripe{position:absolute;left:0;top:0;width:10px;height:100%;background:linear-gradient(var(--brand),#1b5f86)}
.fax .brand{position:absolute;left:24px;top:30px;font-size:10px}
.fax-title{position:absolute;left:22px;top:150px;font-size:20px;font-weight:400;letter-spacing:.5px}
.fax-fields{position:absolute;left:22px;top:185px;width:290px;display:grid;grid-template-columns:1fr 1fr;column-gap:16px;row-gap:7px}
.field{display:flex;align-items:flex-end;font-size:5.5px;color:var(--muted);border-bottom:1px solid var(--rule);height:11px}
.fax-checks{position:absolute;left:22px;top:268px;width:290px;display:flex;justify-content:space-between;font-size:5.5px;color:var(--muted)}
.fax-checks span{display:flex;align-items:center;gap:3px}
.fax-checks i{width:7px;height:7px;border:1px solid var(--muted)}
.fax .swoosh{position:absolute;left:0;bottom:0;width:100%;height:70px}

/* envelope backs */
.envelope--back-blue{left:744px;top:12px;width:432px;height:90px;background:linear-gradient(#eaf6fc,#cfeaf7)}
.envelope--back-dark{left:744px;top:72px;width:432px;height:78px}
.flap{position:absolute;left:0;top:0}

/* envelope fronts */
.envelope--front{left:773px;top:149px;width:403px;height:110px}
.envelope--plain{left:773px;top:307px;width:403px;height:137px}
.envelope--front .brand,.envelope--plain .brand{position:absolute;left:14px;top:16px;font-size:9px}
.envelope .swoosh{position:absolute;left:0;bottom:0;width:100%;height:40px}
.envelope--plain .band{position:absolute;left:0;top:0;width:100%;height:60px}
.envelope .web{position:absolute;left:0;right:0;bottom:6px;text-align:center;font-size:5px;color:var(--muted);z-index:2}

/* cards */
.card{top:494px;height:82px;background:linear-gradient(#24282d,var(--night));color:var(--paper)}
.card--front{left:773px;width:151px}
.card--front .brand{position:absolute;left:12px;top:30px;font-size:8.5px}
.card--back{left:936px;width:132px}
.card--back .brand{position:absolute;left:8px;top:8px;font-size:6.5px}
.card-person{position:absolute;left:8px;top:28px;font-size:5.5px;line-height:1.5;color:#cfd5da}
.card-person strong{font-weight:500;color:var(--paper);font-size:6.5px}
</style>
</head>
<body>

<section class="sheet letterhead" aria-label="Letterhead">
  <svg class="band" viewBox="0 0 320 62" preserveAspectRatio="none">
    <path d="M0 0H320V40Q170 70 0 48Z" fill="var(--night)"/>
    <path d="M0 48Q170 70 320 40V44Q170 74 0 52Z" fill="var(--brand)"/>
  </svg>
  <div class="brand brand--light"><span class="brand-mark"></span>Calibrated NET Systems</div>
  <div class="foot">
    <p>T +1 604 555 0142<br>F +1 604 555 0143</p>
    <p>dean.harlowe@calnet.ca<br>www.calnet.ca</p>
  </div>
</section>

<section class="sheet fax" aria-label="Fax cover sheet">
  <div class="stripe"></div>
  <div class="brand"><span class="brand-mark"></span>Calibrated NET Systems</div>
  <h1 class="fax-title">FAX</h1>
  <div class="fax-fields">
    <div class="field">To:</div><div class="field">From:</div>
    <div class="field">Fax:</div><div class="field">Pages:</div>
    <div class="field">Phone:</div><div class="field">Date:</div>
    <div class="field">Re:</div><div class="field">CC:</div>
  </div>
  <div class="fax-checks">
    <span><i></i>Urgent</span><span><i></i>For Review</span><span><i></i>Please Comment</span><span><i></i>Please Reply</span><span><i></i>Please Recycle</span>
  </div>
  <svg class="swoosh" viewBox="0 0 336 70" preserveAspectRatio="none">
    <path d="M0 40Q170 10 336 30V70H0Z" fill="var(--mist)"/>
  </svg>
  <div class="foot" style="padding-left:22px">
    <p>T +1 604 555 0142<br>F +1 604 555 0143</p>
    <p>dean.harlowe@calnet.ca<br>www.calnet.ca</p>
  </div>
</section>

<div class="envelope envelope--back-blue" aria-label="Envelope back, light">
  <svg class="flap" width="432" height="90" viewBox="0 0 432 90">
    <path d="M0 0L216 58L432 0Z" fill="#9fd3ee"/>
    <path d="M0 0L216 56L432 0" fill="none" stroke="var(--brand)" stroke-width="2"/>
  </svg>
</div>

<div class="envelope envelope--back-dark" aria-label="Envelope back, dark">
  <svg class="flap" width="432" height="78" viewBox="0 0 432 78">
    <path d="M0 0H432L216 60Z" fill="var(--night)"/>
    <path d="M0 0L216 60L432 0" fill="none" stroke="#4a5058" stroke-width="2"/>
  </svg>
</div>

<div class="envelope envelope--front" aria-label="Envelope front">
  <div class="brand"><span class="brand-mark"></span>Calibrated NET Systems</div>
  <svg class="swoosh" viewBox="0 0 403 40" preserveAspectRatio="none">
    <path d="M0 22Q200 0 403 18V40H0Z" fill="var(--mist)"/>
  </svg>
  <p class="web">www.calnet.ca</p>
</div>

<div class="envelope envelope--plain" aria-label="Envelope, alternate">
  <svg class="band" viewBox="0 0 403 60" preserveAspectRatio="none">
    <path d="M0 0H403V34Q200 60 0 40Z" fill="var(--mist)"/>
  </svg>
  <div class="brand"><span class="brand-mark"></span>Calibrated NET Systems</div>
  <svg class="swoosh" viewBox="0 0 403 40" preserveAspectRatio="none">
    <path d="M0 22Q200 0 403 18V40H0Z" fill="var(--mist)"/>
  </svg>
  <p class="web">www.calnet.ca</p>
</div>

<div class="card card--front" aria-label="Business card front">
  <div class="brand brand--light"><span class="brand-mark"></span>Calibrated NET Systems</div>
</div>

<div class="card card--back" aria-label="Business card back">
  <div class="brand brand--light"><span class="brand-mark"></span>Calibrated NET Systems</div>
  <p class="card-person"><strong>Dean Harlowe</strong><br>Technical Consultant<br>T +1 604 555 0142<br>dean.harlowe@calnet.ca<br>www.calnet.ca</p>
</div>

</body>
</html>
```